ROOM REVIVE HQ
With Moira Pennell
Project: ROOM REVIVE HQ
ROOM REVIVE HQ -
Creative Brief
Use specific fonts
Not sure at the moment
Professional
Moira Pennell
Elmcroft Lodge 9 Elmcroft Terrace Hastings East Sussex TN37 6QR
moira@roomrevivehq.co.uk
www.roomrevivehq.co.uk
Company No. 5290418
Thinking of selling, about to reduce the price of your home? Before you do, speak to Moira Pennell at Room Revive HQ to see how Home Staging can help assist in selling your property fast and for the best asking price
Services Home Staging De Cluttering Moving in Moving out House Photography Sourcing accessorise

```html
<!DOCTYPE html>
<html lang="en">
<head>
<meta charset="utf-8">
<title>Room Revive HQ – Stationery</title>
<link rel="stylesheet" href="https://fonts.googleapis.com/css2?family=Open+Sans:ital,wght@0,400;0,600;0,700;1,400&display=swap">
<style>
:root{
  --bg:#e6e1d8;
  --paper:#ffffff;
  --ink:#3a3a3a;
  --ink-soft:#8a8a8a;
  --blue:#1f4fa3;
  --blue-dark:#163a7a;
  --red:#d8262e;
  --line:#c9c9c9;
  --placeholder:#e3e6ec;
  --placeholder-edge:#cfd4dd;
}
*{box-sizing:border-box;margin:0;padding:0}
html,body{width:1200px;height:559px;overflow:hidden}
body{background:var(--bg);font-family:"Open Sans",Arial,sans-serif;color:var(--ink);position:relative}
.sheet{position:absolute;background:var(--paper);box-shadow:0 2px 6px rgba(0,0,0,.25);overflow:hidden}
.emblem{position:absolute;background:var(--placeholder);border:0.6px solid var(--placeholder-edge);border-radius:4px}
.brand{font-weight:700;color:var(--blue);letter-spacing:.3px;line-height:1;white-space:nowrap}
.houses{position:absolute;border-radius:3px 3px 0 0;background:linear-gradient(90deg,#e9a25a 0%,#eccb6a 40%,#8fb0dc 75%,#d86a6e 100%)}
.swoosh{position:absolute;left:0;bottom:0;width:100%}
.body-text{font-size:4.6px;line-height:7px;color:var(--ink-soft);text-align:justify}
.body-text p{margin-bottom:6px}
.small{font-size:4.6px;line-height:6.2px;color:var(--ink)}
.sign{font-size:9px;font-style:italic;color:var(--blue-dark);margin:4px 0 2px}

/* Fax cover */
.fax{left:20px;top:25px;width:310px;height:505px}
.fax .emblem{left:14px;top:12px;width:38px;height:46px}
.fax .brand{position:absolute;left:58px;top:30px;font-size:7px}
.fax .head-text{position:absolute;left:140px;top:14px;width:160px;font-size:4px;line-height:5.5px;color:var(--ink-soft)}
.fax-title{position:absolute;right:16px;top:52px;font-size:7px;font-weight:700;color:var(--ink)}
.fax-table{position:absolute;left:14px;top:62px;width:282px;border-collapse:collapse;font-size:4.6px}
.fax-table td{border:0.6px solid var(--line);height:10px;padding:0 3px}
.fax-table td.label{width:30px;color:var(--ink)}
.fax-checks{position:absolute;left:14px;top:112px;width:282px;display:flex;justify-content:space-between;font-size:4.4px}
.fax-checks span::before{content:"";display:inline-block;width:4px;height:4px;border:0.6px solid var(--ink);margin-right:2px;vertical-align:-0.5px}
.fax .body-text{position:absolute;left:14px;top:130px;width:282px}
.fax .close{position:absolute;left:14px;top:345px}
.fax .houses{right:24px;bottom:34px;width:100px;height:50px}

/* Letterhead */
.letter{left:370px;top:25px;width:310px;height:505px}
.letter .emblem{left:132px;top:10px;width:46px;height:52px}
.letter .contact{position:absolute;right:12px;top:14px;width:110px;text-align:right}
.letter .recipient{position:absolute;left:18px;top:60px}
.letter .body-text{position:absolute;left:18px;top:98px;width:274px}
.letter .close{position:absolute;left:18px;top:345px}
.letter .houses{right:26px;bottom:34px;width:100px;height:50px}

/* Business cards */
.card-front{left:760px;top:25px;width:185px;height:72px}
.card-front .emblem{left:12px;top:10px;width:38px;height:48px}
.card-front .brand{position:absolute;left:56px;top:28px;font-size:9px}
.card-front .tag{position:absolute;left:56px;top:40px;font-size:4.6px;color:var(--ink-soft)}
.card-back{left:962px;top:25px;width:210px;height:72px;background:var(--blue)}
.card-back .info{position:absolute;left:12px;top:10px;color:#fff;font-size:5px;line-height:7px}
.card-back .info strong{font-size:6.5px}
.card-back .emblem{right:12px;top:12px;width:36px;height:44px}

/* Envelopes */
.env-front{left:760px;top:125px;width:412px;height:180px}
.env-front .emblem{left:14px;top:12px;width:40px;height:50px}
.env-front .brand{position:absolute;left:58px;top:26px;font-size:8px}
.env-front .small{position:absolute;left:58px;top:38px;width:160px}
.env-front .houses{right:26px;bottom:28px;width:112px;height:58px}
.env-back{left:760px;top:322px;width:412px;height:208px}
.env-back .flap{position:absolute;inset:0;width:100%;height:100%}
.env-back .emblem{left:186px;top:52px;width:40px;height:50px}
.env-back .brand{position:absolute;left:0;width:100%;top:108px;text-align:center;font-size:8px}
</style>
</head>
<body>

<section class="sheet fax">
  <div class="emblem" role="img" aria-label="Brand character illustration"></div>
  <div class="brand">ROOM REVIVE HQ</div>
  <div class="head-text">Moira Pennell · Elmcroft Lodge 9 Elmcroft Terrace<br>Hastings East Sussex TN37 6QR<br>moira@roomrevivehq.co.uk · www.roomrevivehq.co.uk<br>Company No. 5290418</div>
  <div class="fax-title">FAX</div>
  <table class="fax-table">
    <tr><td class="label">To:</td><td></td><td class="label">From:</td><td></td></tr>
    <tr><td class="label">Fax:</td><td></td><td class="label">Pages:</td><td></td></tr>
    <tr><td class="label">Phone:</td><td></td><td class="label">Date:</td><td></td></tr>
    <tr><td class="label">Re:</td><td></td><td class="label">CC:</td><td></td></tr>
  </table>
  <div class="fax-checks">
    <span>Urgent</span><span>For Review</span><span>Please Comment</span><span>Please Reply</span><span>Please Recycle</span>
  </div>
  <div class="body-text">
    <p>Thank you for choosing us to prepare your home for sale. We stage each room with care so buyers see space, light and comfort from the moment they step inside the door.</p>
    <p>Our team will visit, plan the layout, bring furniture and accessories, and leave every space ready for photos and viewings within a few days.</p>
    <p>Thank you for choosing us to prepare your home for sale. We stage each room with care so buyers see space, light and comfort from the moment they step inside the door.</p>
    <p>Our team will visit, plan the layout, bring furniture and accessories, and leave every space ready for photos and viewings within a few days.</p>
    <p>Thank you for choosing us to prepare your home for sale. We stage each room with care so buyers see space, light and comfort from the moment they step inside the door.</p>
    <p>Our team will visit, plan the layout, bring furniture and accessories, and leave every space ready for photos and viewings within a few days.</p>
    <p>Thank you for choosing us to prepare your home for sale. We stage each room with care so buyers see space, light and comfort from the moment they step inside the door.</p>
  </div>
  <div class="close small">Yours Sincerely,<div class="sign">Moira Pennell</div>Moira Pennell</div>
  <div class="houses" role="img" aria-label="Illustration of colourful houses"></div>
  <svg class="swoosh" viewBox="0 0 310 40" height="40" preserveAspectRatio="none" aria-hidden="true">
    <path d="M0 40 L0 30 Q150 8 310 18 L310 40 Z" fill="var(--blue)"/>
    <path d="M0 34 Q150 14 310 24" stroke="var(--red)" stroke-width="1.5" fill="none"/>
  </svg>
</section>

<section class="sheet letter">
  <div class="emblem" role="img" aria-label="Brand character illustration"></div>
  <div class="contact small">Elmcroft Lodge 9 Elmcroft Terrace<br>Hastings East Sussex TN37 6QR<br>moira@roomrevivehq.co.uk<br>www.roomrevivehq.co.uk</div>
  <div class="recipient small">Alex Example<br>12 Sample Street<br>Brisbane, Australia<br><br>Dear Alex Example,</div>
  <div class="body-text">
    <p>Thank you for choosing us to prepare your home for sale. We stage each room with care so buyers see space, light and comfort from the moment they step inside the door.</p>
    <p>Our team will visit, plan the layout, bring furniture and accessories, and leave every space ready for photos and viewings within a few days.</p>
    <p>Thank you for choosing us to prepare your home for sale. We stage each room with care so buyers see space, light and comfort from the moment they step inside the door.</p>
    <p>Our team will visit, plan the layout, bring furniture and accessories, and leave every space ready for photos and viewings within a few days.</p>
    <p>Thank you for choosing us to prepare your home for sale. We stage each room with care so buyers see space, light and comfort from the moment they step inside the door.</p>
    <p>Our team will visit, plan the layout, bring furniture and accessories, and leave every space ready for photos and viewings within a few days.</p>
    <p>Thank you for choosing us to prepare your home for sale. We stage each room with care so buyers see space, light and comfort from the moment they step inside the door.</p>
  </div>
  <div class="close small">Yours Sincerely,<div class="sign">Moira Pennell</div>Moira Pennell</div>
  <div class="houses" role="img" aria-label="Illustration of colourful houses"></div>
  <svg class="swoosh" viewBox="0 0 310 40" height="40" preserveAspectRatio="none" aria-hidden="true">
    <path d="M0 40 L0 30 Q150 8 310 18 L310 40 Z" fill="var(--blue)"/>
    <path d="M0 34 Q150 14 310 24" stroke="var(--red)" stroke-width="1.5" fill="none"/>
  </svg>
</section>

<section class="sheet card-front">
  <div class="emblem" role="img" aria-label="Brand character illustration"></div>
  <div class="brand">ROOM REVIVE HQ</div>
  <div class="tag">Home Staging · De Cluttering</div>
  <svg class="swoosh" viewBox="0 0 185 14" height="14" preserveAspectRatio="none" aria-hidden="true">
    <path d="M0 14 L0 10 Q90 0 185 6 L185 14 Z" fill="var(--blue)"/>
  </svg>
</section>

<section class="sheet card-back">
  <div class="info"><strong>Moira Pennell</strong><br>Elmcroft Lodge 9 Elmcroft Terrace<br>Hastings East Sussex TN37 6QR<br>moira@roomrevivehq.co.uk<br>www.roomrevivehq.co.uk</div>
  <div class="emblem" role="img" aria-label="Brand character illustration"></div>
</section>

<section class="sheet env-front">
  <div class="emblem" role="img" aria-label="Brand character illustration"></div>
  <div class="brand">ROOM REVIVE HQ</div>
  <div class="small">Elmcroft Lodge 9 Elmcroft Terrace<br>Hastings East Sussex TN37 6QR</div>
  <div class="houses" role="img" aria-label="Illustration of colourful houses"></div>
  <svg class="swoosh" viewBox="0 0 412 34" height="34" preserveAspectRatio="none" aria-hidden="true">
    <path d="M0 34 L0 26 Q200 4 412 14 L412 34 Z" fill="var(--blue)"/>
    <path d="M0 30 Q200 10 412 20" stroke="var(--red)" stroke-width="1.5" fill="none"/>
  </svg>
</section>

<section class="sheet env-back">
  <svg class="flap" viewBox="0 0 412 208" preserveAspectRatio="none" aria-hidden="true">
    <path d="M0 0 L206 120 L412 0" stroke="var(--line)" stroke-width="0.8" fill="none"/>
    <path d="M0 208 L160 100 M412 208 L252 100" stroke="var(--line)" stroke-width="0.8" fill="none"/>
    <path d="M0 208 L0 196 Q200 170 412 184 L412 208 Z" fill="var(--blue)" opacity=".85"/>
  </svg>
  <div class="emblem" role="img" aria-label="Brand character illustration"></div>
  <div class="brand">ROOM REVIVE HQ</div>
</section>

</body>
</html>
```